Harbourline Metro Business Racquet Circuit (est.1952)

The Metro Business Racquet Circuit began in 1952 and has been played every year since. It is the longest running continuous sporting competition in the Sydney CBD. It is a team squash competition from May to Oct yearly played between companies, sporting groups or just a groups of friends.
We are looking for a flyer that we can reuse every year (so the content within the flyer can't be tied to a specific time). Other specific we are looking for are
1. Squash imagery (can either be real or graphic design) depicting action / athleticism / friendly rivalry
2. Needs the following content
a ) "A Sydney CBD based competition for friendly rivalry between companies, sporting clubs or between friends"
b) "All matches in and around the CBD from 5.30pm to 8pm"
c) "We cater for all playing abilities"
d) "Ladies beginner comp includes complimentary coaching"
e) "Visit our website www.plvqn.org.au for more info or contact Walter on frontw@qmx.com.au"

Flyer needs to include the logos attached in file upload section

```html
<!DOCTYPE html>
<html lang="en">
<head>
<meta charset="utf-8">
<title>Harbourline Metro Business Racquet Circuit – Flyer</title>
<link href="https://fonts.googleapis.com/css2?family=Graduate&family=Oswald:wght@500;600&family=Poppins:wght@400;600;700;800&display=swap" rel="stylesheet">
<style>
  :root{
    --stage:#e9e9e9;
    --ink:#2a2a2a;
    --blue:#3a96d8;
    --blue-deep:#2f86c9;
    --yellow:#f7b619;
    --white:#ffffff;
    --grey-text:#cfcfcf;
    --dark-text:#1f1f1f;
  }
  *{box-sizing:border-box;margin:0;padding:0}
  html,body{width:1200px;height:2261px;overflow:hidden;background:var(--stage)}
  body{position:relative;font-family:"Poppins",sans-serif}

  .flyer{position:absolute;left:100px;top:423px;width:1000px;height:1414px;background:var(--ink);overflow:hidden;box-shadow:0 14px 30px rgba(0,0,0,.25)}

  .hero-photo{position:absolute;left:470px;top:60px;width:530px;height:790px;
    background:
      radial-gradient(ellipse at 62% 30%, #a8a8a8 0 14%, rgba(168,168,168,0) 34%),
      radial-gradient(ellipse at 55% 50%, rgba(247,182,25,.95) 0 40%, rgba(247,182,25,0) 68%),
      linear-gradient(160deg,#3c3c3c 0%,#2a2a2a 100%);
    border-radius:45% 0 40% 55%}

  .brand{position:absolute;left:72px;top:110px;display:flex;align-items:center;gap:14px}
  .brand-dot{width:44px;height:44px;border-radius:50%;background:var(--blue)}
  .brand-name{font-weight:800;font-size:34px;color:var(--white);letter-spacing:.5px}

  .banner{position:absolute;left:42px;top:250px;width:624px;height:140px;background:var(--blue);
    clip-path:polygon(2% 0,100% 12%,97% 100%,0 100%);padding:30px 0 0 36px;border-left:6px solid var(--white)}
  .banner-kicker{font-weight:800;font-size:33px;color:var(--ink);line-height:1;text-transform:uppercase}
  .banner-title{font-weight:800;font-size:50px;color:var(--white);line-height:1.1;text-transform:uppercase}

  .title{position:absolute;left:72px;top:420px;font-family:"Graduate",serif;font-weight:400;line-height:.95}
  .title-line{display:block;font-size:86px}
  .title-line.grey{color:#d6d6d6}
  .title-line.blue{color:var(--blue)}
  .title-line.yellow{color:var(--yellow)}
  .title-sub{display:block;font-family:"Poppins",sans-serif;font-weight:800;font-size:24px;letter-spacing:14px;color:var(--white);margin-top:8px}
  .est{position:absolute;left:72px;top:728px;font-size:26px;color:var(--grey-text)}

  .intro{position:absolute;left:72px;top:918px;width:590px;font-size:19px;line-height:1.2;color:var(--white)}
  .ladies{position:absolute;left:72px;top:988px;width:394px;height:43px;border:2px solid var(--blue);
    font-family:"Oswald",sans-serif;font-weight:500;font-size:27px;color:var(--white);text-align:center;line-height:39px;text-transform:uppercase;white-space:nowrap}
  .coaching{position:absolute;left:487px;top:984px;color:var(--yellow);text-transform:uppercase;font-weight:800}
  .coaching small{display:block;font-size:16px;line-height:1.1}
  .coaching strong{display:block;font-size:29px;line-height:1}

  .info{position:absolute;left:703px;top:0;width:240px;height:1414px;color:var(--white);text-align:center;white-space:nowrap}
  .info > *{position:absolute;left:0;width:100%}
  .info-kicker{top:914px;font-weight:700;font-size:29px;color:var(--yellow);line-height:1}
  .info-line{top:946px;font-size:25px;line-height:1}
  .info-big{top:970px;font-family:"Oswald",sans-serif;font-weight:600;font-size:80px;line-height:1.05}
  .info-from{top:1052px;display:flex;align-items:center;gap:8px;font-size:20px;line-height:1}
  .info-from::before,.info-from::after{content:"";flex:1;height:2px;background:var(--white)}
  .time-tag{top:1085px;left:12px;width:216px;height:50px;background:var(--blue);
    clip-path:polygon(3% 0,100% 0,97% 100%,0 100%);font-family:"Oswald",sans-serif;font-weight:500;font-size:32px;line-height:50px}
  .time-tag em{font-style:normal;font-size:21px}
  .dotted{top:1180px;border-top:3px dotted var(--white)}
  .cater-kicker{top:1226px;font-weight:700;font-size:21px;color:var(--yellow);line-height:1}
  .cater-big{top:1246px;font-family:"Oswald",sans-serif;font-weight:600;font-size:70px;line-height:1}
  .cater-sub{top:1322px;font-size:27px;letter-spacing:7px;line-height:1}

  .crowd-photo{position:absolute;left:190px;top:1000px;width:510px;height:414px;
    background:linear-gradient(180deg,rgba(42,42,42,1) 0%,#454545 45%,#575757 100%)}
  .contact-panel{position:absolute;left:0;top:1000px;width:700px;height:414px}

  .contact{position:absolute;left:72px;top:1158px;color:var(--dark-text)}
  .contact-label{font-size:18px;line-height:1.2}
  .contact-email{font-weight:700;font-size:30px;line-height:1.15}
  .contact-url{font-weight:800;font-size:34px;line-height:1.15}
  .contact-url span{color:var(--blue-deep)}
  .contact-gap{height:10px}

  .partners{position:absolute;left:72px;top:1310px;display:flex;align-items:center;gap:20px}
  .badge-round{width:60px;height:60px;border-radius:50%;background:#1d2b57;border:3px solid #c9a23a}
  .badge-small{width:32px;height:32px;border-radius:50%;background:#e25a3a}
  .partner-text{font-family:"Oswald",sans-serif;font-weight:500;font-size:13px;color:var(--dark-text);text-transform:uppercase}
  .partner-text b{color:#d8262f;font-weight:500}
  .partner-mark{display:flex;align-items:center;gap:8px}
  .partner-mark i{display:block;width:28px;height:28px;background:var(--blue-deep)}
</style>
</head>
<body>
  <main class="flyer">
    <div class="hero-photo" role="img" aria-label="Black and white photo of a female squash player lunging forward with her racquet over a yellow paint splash"></div>

    <div class="brand">
      <span class="brand-dot"></span>
      <span class="brand-name">Harbourline Squash</span>
    </div>

    <div class="banner">
      <p class="banner-kicker">Harbourline</p>
      <p class="banner-title">Competition for</p>
    </div>

    <h1 class="title">
      <span class="title-line grey">METRO</span>
      <span class="title-line blue">BUSINESS</span>
      <span class="title-line yellow">RACQUET</span>
      <span class="title-sub">CIRCUIT</span>
    </h1>
    <p class="est">(est.1952)</p>

    <div class="crowd-photo" role="img" aria-label="Black and white photo of players celebrating a match together"></div>
    <svg class="contact-panel" viewBox="0 0 700 414" aria-hidden="true">
      <path fill="#ffffff" d="M0 60 L28 42 L42 72 L66 22 L92 58 L128 50 L158 82 L198 66 L236 98 L290 94 L340 116 L390 122 L430 146 L452 180 L470 210 L505 214 L492 244 L540 256 L528 292 L575 302 L610 330 L650 345 L700 400 L700 414 L0 414 Z"/>
    </svg>

    <p class="intro">A Sydney CBD based competition for friendly rivalry between companies, sporting clubs or between friends</p>
    <p class="ladies">Ladies beginner comp includes</p>
    <p class="coaching"><small>Complimentary</small><strong>Coaching</strong></p>

    <section class="info">
      <p class="info-kicker">ALL MATCHES</p>
      <p class="info-line">IN AND AROUND</p>
      <p class="info-big">THE CBD</p>
      <p class="info-from">from</p>
      <span class="time-tag">5.30PM <em>TO</em> 8PM</span>
      <div class="dotted"></div>
      <p class="cater-kicker">WE CATER FOR ALL</p>
      <p class="cater-big">PLAYING</p>
      <p class="cater-sub">ABILITIES</p>
    </section>

    <section class="contact">
      <p class="contact-label">For more info or contact <strong>Walter</strong> on</p>
      <p class="contact-email">frontw@qmx.com.au</p>
      <div class="contact-gap"></div>
      <p class="contact-label">Visit our website</p>
      <p class="contact-url">www.<span>plvqn.org</span>.au</p>
    </section>

    <div class="partners">
      <span class="badge-round"></span>
      <span class="badge-small"></span>
      <span class="partner-text">Quayside Courts <b>Racquets</b> Association</span>
      <span class="partner-mark"><i></i><span class="partner-text">Northshore Racquet Academy</span></span>
    </div>
  </main>
</body>
</html>
```